Business Cards and Stationary for Studio Calmaris (Massage Therapy)
BC for Massage Therapy Studio
Professional
Corwin Palde
President/CEO
742 Fenwick Rd.
Ste. 7C
Greer, SC 48213
cpalde@studiocalmaris.example
www.studiocalmaris.example
Logo AI file

```html
<!DOCTYPE html>
<html lang="en">
<head>
<meta charset="utf-8">
<title>Studio Calmaris — Business Card</title>
<link href="https://fonts.googleapis.com/css2?family=Libre+Baskerville:wght@400;700&display=swap" rel="stylesheet">
<style>
  :root {
    --backdrop: #e4e5e7;
    --card: #0b0b0b;
    --gold: #e8d417;
    --text: #e9e9e9;
    --mark-faint: #4a4a4a;
  }
  * { box-sizing: border-box; margin: 0; padding: 0; }
  html, body { width: 1200px; height: 648px; overflow: hidden; }
  body {
    background: var(--backdrop);
    font-family: "Libre Baskerville", "Times New Roman", serif;
    position: relative;
  }
  .card {
    position: absolute;
    top: 159px;
    width: 555px;
    height: 330px;
    background: var(--card);
    border-radius: 22px;
    overflow: hidden;
  }
  .card--front { left: 30px; }
  .card--back { left: 615px; }

  .front-mark {
    position: absolute;
    left: -120px;
    top: 120px;
    width: 250px;
    height: 250px;
    border-radius: 50%;
    background: var(--mark-faint);
    display: flex;
    align-items: center;
    justify-content: flex-end;
    padding-right: 18px;
  }
  .front-mark__name {
    color: var(--card);
    font-size: 13px;
    width: 90px;
    line-height: 1.3;
  }

  .studio-title {
    position: absolute;
    left: 262px;
    top: 56px;
    color: var(--gold);
    font-size: 27px;
    font-weight: 400;
    font-variant: small-caps;
    letter-spacing: 0.5px;
    white-space: nowrap;
  }
  .studio-rule {
    position: absolute;
    left: 262px;
    top: 96px;
    width: 268px;
    height: 2px;
    background: var(--gold);
  }
  .contact {
    position: absolute;
    left: 318px;
    top: 135px;
    color: var(--text);
    font-size: 10px;
    line-height: 1.45;
  }
  .contact__name { color: var(--gold); }
  .contact__group { margin-bottom: 14px; }
  .website {
    position: absolute;
    left: 318px;
    top: 285px;
    color: var(--text);
    font-size: 10px;
  }

  .back-mark {
    position: absolute;
    left: 50%;
    top: 50%;
    transform: translate(-50%, -50%);
    display: flex;
    flex-direction: column;
    align-items: center;
    gap: 14px;
  }
  .back-mark__disc {
    width: 118px;
    height: 118px;
    border-radius: 50%;
    background: var(--gold);
  }
  .back-mark__name {
    color: var(--gold);
    font-size: 16px;
    font-variant: small-caps;
    letter-spacing: 0.5px;
    white-space: nowrap;
  }
</style>
</head>
<body>
  <section class="card card--front" aria-label="Card front">
    <div class="front-mark"><span class="front-mark__name">Studio Calmaris</span></div>
    <h1 class="studio-title">Studio Calmaris</h1>
    <div class="studio-rule"></div>
    <div class="contact">
      <div class="contact__group">
        <p class="contact__name">Corwin Palde</p>
        <p>President/CEO</p>
      </div>
      <div class="contact__group">
        <p>742 Fenwick Rd., Ste. 7C</p>
        <p>Halden, OR 48213</p>
      </div>
      <div class="contact__group">
        <p>P: 555.201.0172</p>
        <p>E: cpalde@studiocalmaris.example</p>
      </div>
    </div>
    <p class="website">www.studiocalmaris.example</p>
  </section>

  <section class="card card--back" aria-label="Card back">
    <div class="back-mark">
      <div class="back-mark__disc"></div>
      <span class="back-mark__name">Studio Calmaris</span>
    </div>
  </section>
</body>
</html>
```